Event Materials for Charity's 10th Anniversary Dinner

We are a charity celebrating our 10th Anniversary with a dinner. We need three editable designs for the following -

Name tags - 90mm x 55m graphic file only in pdf at 100% size. Must be able to merge from Excel.

Place cards - 90mm x 120mm (folded to 90mm x 60mm) graphic file only in pdf at 100% size. Must be able to merge from Excel.

Table number cards - A6 size to be placed in a table number stand. Must have space for the table number in addition to company names and logo

They must all have the same theme including our 10 year anniversary logo and our blue water colour brush stroke theme which can be stretched.

I am attaching a copy of the invitation so that the theme can be followed as well as a graphic of the watercolour. I am attaching three versions of our anniversary logo, including their reverse logo. Please use whichever one you think looks best.

Target Market(s)

Attendees

Industry/Entity Type

Charity

Font styles to use
Serif

Colors
0054AA
0677BA
7BADD7
CADEEF
E8F1F8

Requirements
Must have
• Logo and the provided blue watercolour graphic

```html
<!DOCTYPE html>
<html lang="en">
<head>
<meta charset="utf-8">
<title>Anniversary Dinner – Event Stationery</title>
<link rel="stylesheet" href="https://fonts.googleapis.com/css2?family=Cormorant+Garamond:wght@500;600;700&family=Montserrat:wght@600;700&display=swap">
<style>
  :root {
    --page-bg: #e8edf4;
    --paper: #ffffff;
    --ink: #0b0b0b;
    --wash-deep: #1d4590;
    --wash-mid: #2f62ad;
    --wash-light: #5b8bd0;
    --wash-pale: #cadeef;
    --on-wash: #ffffff;
  }
  * { box-sizing: border-box; margin: 0; padding: 0; }
  html, body { width: 1200px; height: 802px; overflow: hidden; }
  body { background: var(--page-bg); position: relative; }

  .watercolour {
    position: absolute;
    background:
      radial-gradient(ellipse 60% 70% at 35% 65%, rgba(91,139,208,.85), rgba(91,139,208,0) 70%),
      radial-gradient(ellipse 40% 50% at 8% 10%, rgba(202,222,239,.9), rgba(202,222,239,0) 70%),
      linear-gradient(120deg, var(--wash-mid) 0%, var(--wash-deep) 60%, var(--wash-deep) 100%);
  }

  .brand {
    position: absolute;
    color: var(--on-wash);
    font-family: "Cormorant Garamond", serif;
    font-weight: 600;
    text-align: center;
    line-height: 1.1;
  }
  .brand__mark {
    display: inline-block;
    width: 14px; height: 14px;
    border: 2px solid var(--on-wash);
    vertical-align: middle;
    margin-right: 6px;
  }

  /* Name tag */
  .name-tag {
    position: absolute; left: 54px; top: 17px;
    width: 471px; height: 287px;
    background: var(--paper);
  }
  .name-tag .watercolour { left: 0; top: 0; width: 100%; height: 155px; }
  .name-tag .brand { right: 22px; top: 50px; width: 130px; font-size: 17px; }

  .person-name {
    font-family: "Montserrat", sans-serif;
    font-weight: 700;
    color: var(--ink);
    text-align: center;
    white-space: nowrap;
    letter-spacing: .2px;
  }
  .person-title {
    font-family: "Montserrat", sans-serif;
    font-weight: 600;
    color: var(--ink);
    text-align: center;
  }
  .name-tag .person-name { position: absolute; left: 0; right: 0; top: 186px; font-size: 46px; line-height: 1; }
  .name-tag .person-title { position: absolute; left: 0; right: 0; top: 248px; font-size: 24px; line-height: 1; }

  /* Table number card */
  .table-card {
    position: absolute; left: 147px; top: 322px;
    width: 325px; height: 457px;
    background: var(--paper);
  }
  .table-card .watercolour { left: 0; top: 113px; width: 100%; height: 344px; }
  .sponsors {
    position: absolute; left: 0; right: 0; top: 28px;
    font-family: "Cormorant Garamond", serif;
    font-weight: 500;
    font-size: 21px;
    line-height: 28px;
    letter-spacing: 1.6px;
    text-align: center;
    color: var(--ink);
  }
  .table-label {
    position: absolute; left: 0; right: 0; top: 122px;
    font-family: "Cormorant Garamond", serif;
    font-weight: 600;
    font-size: 60px;
    line-height: 1;
    letter-spacing: 4px;
    text-align: center;
    color: var(--on-wash);
  }
  .table-number {
    position: absolute; left: 0; right: 0; top: 168px;
    font-family: "Cormorant Garamond", serif;
    font-weight: 700;
    font-size: 262px;
    font-variant-numeric: lining-nums;
    line-height: 1;
    text-align: center;
    color: var(--on-wash);
    letter-spacing: -6px;
  }
  .table-card .brand { left: 0; right: 0; top: 415px; font-size: 13px; }

  /* Place card (folded) */
  .place-card {
    position: absolute; left: 662px; top: 31px;
    width: 434px; height: 578px;
  }
  .place-card__half {
    position: absolute; left: 0; width: 100%; height: 289px;
    background: var(--paper);
  }
  .place-card__half--back { top: 0; transform: rotate(180deg); }
  .place-card__half--front { top: 289px; }
  .place-card__half .watercolour { left: 0; top: 0; width: 100%; height: 167px; }
  .place-card__half .brand { left: 0; right: 0; top: 60px; font-size: 17px; }
  .place-card__half .person-name { position: absolute; left: 0; right: 0; top: 190px; font-size: 43px; line-height: 1; }
  .place-card__half .person-title { position: absolute; left: 0; right: 0; top: 248px; font-size: 23px; line-height: 1; }
  .place-card__half--back .watercolour { transform: scaleX(-1); }
</style>
</head>
<body>

  <section class="name-tag" aria-label="Name tag">
    <div class="watercolour" role="img" aria-label="Blue watercolour brush stroke background"></div>
    <div class="brand"><span class="brand__mark"></span>Meridian Giving Trust</div>
    <p class="person-name">NAME GOES HERE</p>
    <p class="person-title">title goes here</p>
  </section>

  <section class="table-card" aria-label="Table number card">
    <p class="sponsors">HERE COMPANY NAMES<br>&amp; LOGOS OF SPONSORS</p>
    <div class="watercolour" role="img" aria-label="Blue watercolour brush stroke background"></div>
    <p class="table-label">TABLE</p>
    <p class="table-number">10</p>
    <div class="brand"><span class="brand__mark"></span>Meridian Giving Trust</div>
  </section>

  <section class="place-card" aria-label="Folded place card">
    <div class="place-card__half place-card__half--back">
      <div class="watercolour" role="img" aria-label="Blue watercolour brush stroke background"></div>
      <div class="brand"><span class="brand__mark"></span>Meridian Giving Trust</div>
      <p class="person-name">NAME GOES HERE</p>
      <p class="person-title">title goes here</p>
    </div>
    <div class="place-card__half place-card__half--front">
      <div class="watercolour" role="img" aria-label="Blue watercolour brush stroke background"></div>
      <div class="brand"><span class="brand__mark"></span>Meridian Giving Trust</div>
      <p class="person-name">NAME GOES HERE</p>
      <p class="person-title">title goes here</p>
    </div>
  </section>

</body>
</html>
```